I need a SEO-friendly Wordpress website (making sure to style H1, H2, H3, etc correctly) for a Hawaii-based law firm called Meridale Crown Legal Group. Comparable websites include https://brvtlaw.com/ and https://www.lorvin.com/ for design reference. The current copy on the TuvellAttorney.com website can be used.

Coding

Coded - Design and coding required

```html
<!DOCTYPE html>
<html lang="en">
<head>
<meta charset="utf-8">
<title>Meridale Crown Legal Group</title>
<link href="https://fonts.googleapis.com/css2?family=Libre+Baskerville:wght@700&family=Poppins:wght@400;500;600;700&family=Open+Sans:wght@400;600&display=swap" rel="stylesheet">
<style>
:root{
  --orange:#d9822b;
  --orange-dark:#b8621a;
  --brown:#7a3a10;
  --nav-a:#8a4513;
  --nav-b:#c56d22;
  --ink:#2b2b2b;
  --muted:#8a8a8a;
  --light:#f2f2f2;
  --dark:#3a3a3a;
  --white:#ffffff;
}
*{box-sizing:border-box;margin:0;padding:0}
html,body{width:1200px;height:2728px;overflow:hidden}
body{position:relative;background:var(--white);font-family:"Open Sans",sans-serif;color:var(--ink)}
section,header,nav,footer{position:absolute;left:0;width:1200px}
.site-header{top:0;height:120px}
.brand{position:absolute;left:76px;top:36px;font-family:"Libre Baskerville",serif;font-weight:700;font-size:34px;color:#1d1d1d}
.header-phone{position:absolute;left:700px;top:42px;font-family:"Poppins",sans-serif;font-weight:600;font-size:22px;color:var(--ink);display:flex;align-items:center;gap:12px}
.btn{display:inline-block;background:var(--orange);color:var(--white);font-family:"Poppins",sans-serif;font-weight:500;text-transform:uppercase;text-align:center;border-radius:4px}
.header-cta{position:absolute;left:918px;top:30px;width:206px;height:52px;line-height:52px;font-size:19px}
.main-nav{top:120px;height:60px;background:linear-gradient(90deg,var(--nav-a),var(--nav-b));display:flex;align-items:center;padding-left:76px}
.main-nav a{color:var(--white);font-family:"Poppins",sans-serif;font-size:17px;font-weight:500;text-decoration:none;margin-right:58px;text-transform:uppercase}
.social{position:absolute;right:76px;top:18px;display:flex;gap:40px}
.social span{width:24px;height:24px;border-radius:50%;background:rgba(255,255,255,.85)}
.hero{top:180px;height:580px}
.hero-photo{position:absolute;inset:0;background:linear-gradient(135deg,#5b5048,#8c7f73 45%,#4a423c)}
.hero h1{position:absolute;left:0;width:1200px;top:196px;text-align:center;color:var(--white);font-family:"Poppins",sans-serif;font-weight:700;font-size:54px;line-height:66px}
.hero-arrow{position:absolute;top:268px;width:56px;height:56px;border-radius:50%;background:rgba(255,255,255,.35)}
.hero-arrow.prev{left:32px}.hero-arrow.next{right:32px}
.hero-arrow svg{position:absolute;left:18px;top:18px}
.section-title{position:absolute;width:1200px;text-align:center;font-family:"Poppins",sans-serif;font-weight:500;font-size:40px;color:var(--ink)}
.title-dot{position:absolute;left:594px;width:12px;height:12px;border-radius:50%;background:var(--orange)}
.practice{top:760px;height:540px}
.practice-item{position:absolute;top:170px;width:240px;text-align:center}
.practice-icon{width:104px;height:104px;margin:0 auto;border-radius:50%;background:#f6e9dc;border:2px solid #ecd2b8}
.practice-item h3{margin-top:30px;font-family:"Poppins",sans-serif;font-weight:500;font-size:21px;color:var(--orange-dark)}
.practice-item p{margin-top:12px;font-size:14px;line-height:22px;color:var(--muted)}
.read-more{display:block;margin-top:14px;font-family:"Poppins",sans-serif;font-size:14px;font-weight:500;color:var(--orange);text-decoration:underline}
.about{top:1300px;height:520px;background:var(--light);overflow:hidden}
.about-accent{position:absolute;right:0;top:0}
.about h2{position:absolute;left:76px;top:60px;font-family:"Poppins",sans-serif;font-weight:500;font-size:44px}
.about-rule{position:absolute;left:76px;top:126px;width:80px;height:4px;background:var(--orange)}
.about h3{position:absolute;left:76px;top:146px;font-family:"Poppins",sans-serif;font-weight:500;font-size:19px;color:var(--orange-dark)}
.about p{position:absolute;left:76px;top:190px;width:480px;font-size:15px;line-height:25px;color:#555}
.about-btn{position:absolute;left:76px;top:378px;width:132px;height:50px;line-height:50px;font-size:17px}
.about-photo{position:absolute;left:620px;top:76px;width:500px;height:356px;background:linear-gradient(135deg,#d8d2cb,#8a8580 60%,#5c5853);border:6px solid var(--white)}
.feed{top:1820px;height:400px}
.post{position:absolute;top:160px;width:520px;display:flex}
.post-date{flex:none;width:80px;font-family:"Poppins",sans-serif;color:var(--orange-dark);text-align:center;border-right:3px solid var(--orange);padding-right:10px}
.post-date .day{display:block;font-size:48px;font-weight:600;line-height:52px}
.post-date .mon{display:block;font-size:18px;font-weight:600;text-transform:uppercase}
.post-date .yr{display:block;font-size:16px;color:var(--muted)}
.post-body{padding-left:22px}
.post-body h3{font-family:"Poppins",sans-serif;font-weight:500;font-size:17px;color:var(--ink);line-height:26px;white-space:nowrap}
.post-body p{margin-top:8px;font-size:14px;line-height:22px;color:var(--muted)}
.post-body .read-more{margin-top:6px}
.contact{top:2220px;height:452px;background:var(--dark)}
.contact .section-title{color:var(--white);top:54px}
.office{position:absolute;left:76px;top:170px;width:300px;color:#ddd}
.office h3{font-family:"Poppins",sans-serif;font-weight:500;font-size:22px;line-height:30px;color:var(--orange)}
.office-line{display:flex;gap:14px;margin-top:22px;font-size:14px;line-height:22px}
.office-line svg{flex:none;margin-top:2px}
.contact-form .field{position:absolute;background:var(--white);border-radius:4px;font-size:15px;color:#9a9a9a;padding:16px 18px}
.submit{position:absolute;left:784px;top:316px;width:338px;height:60px;line-height:60px;font-size:18px}
.site-footer{top:2672px;height:56px;background:var(--orange);color:var(--white);text-align:center;line-height:56px;font-size:14px}
</style>
</head>
<body>

<header class="site-header">
  <div class="brand">Meridale Crown Legal Group</div>
  <div class="header-phone">
    <svg width="24" height="24" viewBox="0 0 24 24"><path d="M6.6 10.8a15 15 0 0 0 6.6 6.6l2.2-2.2c.3-.3.7-.4 1-.2 1.1.4 2.3.6 3.6.6.6 0 1 .4 1 1V20c0 .6-.4 1-1 1A17 17 0 0 1 3 4c0-.6.4-1 1-1h3.5c.6 0 1 .4 1 1 0 1.3.2 2.5.6 3.6.1.3 0 .7-.2 1z" fill="#d9822b"/></svg>
    +1.808.555.0142
  </div>
  <a class="btn header-cta">Free Consultant</a>
</header>

<nav class="main-nav">
  <a>Home</a><a>Practice Areas</a><a>Attorneys</a><a>Blog</a><a>Contact Us</a>
  <div class="social"><span></span><span></span><span></span><span></span></div>
</nav>

<section class="hero">
  <div class="hero-photo" role="img" aria-label="Attorney in a suit meeting with clients at a desk"></div>
  <h1>Dedicated to making sure<br>you receive the care and<br>attention you need.</h1>
  <div class="hero-arrow prev"><svg width="20" height="20" viewBox="0 0 20 20"><path d="M13 3 6 10l7 7" stroke="#fff" stroke-width="3" fill="none"/></svg></div>
  <div class="hero-arrow next"><svg width="20" height="20" viewBox="0 0 20 20"><path d="m7 3 7 7-7 7" stroke="#fff" stroke-width="3" fill="none"/></svg></div>
</section>

<section class="practice">
  <h2 class="section-title" style="top:70px">Practice Areas</h2>
  <div class="title-dot" style="top:130px"></div>
  <div class="practice-item" style="left:90px">
    <div class="practice-icon" role="img" aria-label="Family icon"></div>
    <h3>Family &amp; Divorce</h3>
    <p>Our lawyers handle all aspects of family law on the Big Island and neighboring islands.</p>
    <a class="read-more">Read More</a>
  </div>
  <div class="practice-item" style="left:350px">
    <div class="practice-icon" role="img" aria-label="Injured person icon"></div>
    <h3>Personal Injury</h3>
    <p>Dealing with personal injury and wrongful death claims is hard enough on the victims.</p>
    <a class="read-more">Read More</a>
  </div>
  <div class="practice-item" style="left:610px">
    <div class="practice-icon" role="img" aria-label="Business buildings icon"></div>
    <h3>Corporate &amp; IP</h3>
    <p>The attorneys at our firm have been helping Big Island businesses work with all their legal needs.</p>
    <a class="read-more">Read More</a>
  </div>
  <div class="practice-item" style="left:870px">
    <div class="practice-icon" role="img" aria-label="Real estate building icon"></div>
    <h3>Real Estate</h3>
    <p>Our lawyers work with home owners, buyers and property developers to ensure fair deals.</p>
    <a class="read-more">Read More</a>
  </div>
</section>

<section class="about">
  <svg class="about-accent" width="520" height="520" viewBox="0 0 520 520"><polygon points="520,0 520,520 320,520 150,520 520,60" fill="#7a3a10"/><polygon points="380,0 520,0 520,60 150,520 40,520" fill="#9a4a15"/></svg>
  <h2>About Us</h2>
  <div class="about-rule"></div>
  <h3>Lawyers Serving the Big Island and Neighboring Islands</h3>
  <p>The experienced attorneys at our Kona firm serve clients with a wide range of legal matters, including family law, divorce and custody, personal injury, business formation, intellectual property and real estate. Our offices handle commercial and hospitality matters on behalf of a wide variety of clients, including individuals.</p>
  <a class="btn about-btn">Read More</a>
  <div class="about-photo" role="img" aria-label="Lawyers meeting with a family around an office table"></div>
</section>

<section class="feed">
  <h2 class="section-title" style="top:44px">Latest Feed</h2>
  <div class="title-dot" style="top:104px"></div>
  <article class="post" style="left:80px">
    <div class="post-date"><span class="day">30</span><span class="mon">July</span><span class="yr">2015</span></div>
    <div class="post-body">
      <h3>Top 10 Things To Do Before Filing for Divorce</h3>
      <p>We are good rounded with the intention of helping you through the divorce process and every step of it.</p>
      <a class="read-more">Read More</a>
    </div>
  </article>
  <article class="post" style="left:620px">
    <div class="post-date"><span class="day">31</span><span class="mon">July</span><span class="yr">2015</span></div>
    <div class="post-body">
      <h3>Top 15 Things to Do During Custody Battle</h3>
      <p>It's already tough enough when two people who planned on spending their lives together no longer see eye to eye.</p>
      <a class="read-more">Read More</a>
    </div>
  </article>
</section>

<section class="contact">
  <h2 class="section-title">Contact Us Now</h2>
  <div class="office">
    <h3>Kona Lawyers of Meridale Crown Legal Group</h3>
    <div class="office-line">
      <svg width="16" height="20" viewBox="0 0 16 20"><path d="M8 0a7 7 0 0 0-7 7c0 5 7 13 7 13s7-8 7-13a7 7 0 0 0-7-7zm0 10a3 3 0 1 1 0-6 3 3 0 0 1 0 6z" fill="#d9822b"/></svg>
      <span>74-2210 Palani Drive, Suite 118, Kailua Kona, Hawaii 96740</span>
    </div>
    <div class="office-line">
      <svg width="16" height="16" viewBox="0 0 24 24"><path d="M6.6 10.8a15 15 0 0 0 6.6 6.6l2.2-2.2c.3-.3.7-.4 1-.2 1.1.4 2.3.6 3.6.6.6 0 1 .4 1 1V20c0 .6-.4 1-1 1A17 17 0 0 1 3 4c0-.6.4-1 1-1h3.5c.6 0 1 .4 1 1 0 1.3.2 2.5.6 3.6.1.3 0 .7-.2 1z" fill="#d9822b"/></svg>
      <span>+1.808.555.0142</span>
    </div>
    <div class="office-line">
      <svg width="16" height="14" viewBox="0 0 16 14"><rect x="0.5" y="1" width="15" height="12" fill="none" stroke="#d9822b" stroke-width="1.5"/><path d="m1 2 7 6 7-6" fill="none" stroke="#d9822b" stroke-width="1.5"/></svg>
      <span>clients@meridalecrownlegal.com</span>
    </div>
  </div>
  <form class="contact-form">
    <div class="field" style="left:424px;top:160px;width:344px;height:60px">Name :</div>
    <div class="field" style="left:424px;top:238px;width:344px;height:60px">Phone :</div>
    <div class="field" style="left:424px;top:316px;width:344px;height:60px">E-mail :</div>
    <div class="field" style="left:784px;top:160px;width:338px;height:138px">Message / comment :</div>
  </form>
  <a class="btn submit">Submit Now</a>
</section>

<footer class="site-footer">Copyright © Meridale Crown Legal Group. All Rights Reserved.</footer>

</body>
</html>
```